BRAND NEW EVENT LANTERN TIDE BOAT PARTY FLYER/POSTER

Lantern Tide
Presents:
The Lantern Tide Boat Party
Launch date: 18.05.22
We need a flyer/poster making to advertise our new boat party launching this summer in Ibiza. We are going all-out with the event, therefore we need to showcase this in our advertisement.
We have some of Ibiza's most famous resident DJs playing house/tech music for 4 hours on the boat, which leaves from San Antonio in Ibiza at 5.30pm. The boat holds 200 people!
There will also be professional dancers, who will perform a fire show LED show and act as VIP hostesses for guests. We will also have a full film crew who will be making a promotional video for us on the day.
Feel free to include some, all of none of the above. Be creative!
The poster needs to scream a VIP, high-end boat party with good music and good vibes. It needs to look professional and resonate with who we are - Lantern Tide. It needs to be classy and memorable.
I'm open to ideas! I've included our logo and some photos of the boat/Ibiza in general for inspirational purposes.
Please use your own initiative and don’t just use the photos I’ve sent with some simple writing on it. 😉
Please let me know what you come up with - we need something urgently!
Kind regards,
Lantern Tide Team
Young party-goers on holiday in Ibiza
Events

```html
<!DOCTYPE html>
<html lang="en">
<head>
<meta charset="utf-8">
<title>Lantern Tide Boat Party</title>
<link rel="stylesheet" href="https://fonts.googleapis.com/css2?family=Montserrat:wght@500;700;800;900&family=Allura&display=swap">
<style>
  :root {
    --page: #ffffff;
    --sky-top: #f1f0f6;
    --lavender: #c9b8e0;
    --violet: #8a63b4;
    --purple-deep: #55287e;
    --ink: #1c1a22;
    --white: #ffffff;
    --magenta: #c646d6;
    --orange: #f39421;
    --coral: #e2665a;
    --pink: #d25a86;
    --plank: #e8742a;
    --plank-dark: #c95a1c;
    --sea: #4fb6e2;
    --sea-deep: #2a6ea8;
    --rock: #7c87b8;
  }
  * { margin: 0; padding: 0; box-sizing: border-box; }
  html, body { width: 849px; height: 1200px; overflow: hidden; background: var(--page); }
  .canvas { position: relative; width: 849px; height: 1200px; background: var(--page); }
  .poster {
    position: absolute; left: 45px; top: 63px; width: 762px; height: 1116px; overflow: hidden;
    background: linear-gradient(180deg, var(--sky-top) 0%, #ebe8f2 38%, var(--lavender) 58%, var(--violet) 78%, var(--purple-deep) 100%);
    box-shadow: 0 3px 8px rgba(0,0,0,.35);
  }
  .brand {
    position: absolute; left: 0; right: 0; top: 76px; text-align: center;
    font-family: "Montserrat", sans-serif; font-weight: 800; font-size: 30px; line-height: 36px;
    color: var(--magenta); letter-spacing: 1px;
  }
  .brand-dot {
    display: inline-block; width: 12px; height: 12px; border-radius: 50%;
    background: var(--magenta); margin-right: 10px; vertical-align: middle;
  }
  .presents {
    position: absolute; left: 0; right: 0; top: 176px; text-align: center;
    font-family: "Montserrat", sans-serif; font-weight: 800; font-size: 15px; line-height: 18px;
    letter-spacing: 4px; color: var(--ink);
  }
  .boat-photo {
    position: absolute; left: 86px; top: 206px; width: 602px; height: 348px;
    background: linear-gradient(180deg, #bfe3f5 0%, var(--rock) 30%, var(--sea) 50%, var(--sea-deep) 78%, #3b4f7a 100%);
    border-radius: 40px 60px 30px 50px;
  }
  .headline { position: absolute; left: 62px; top: 545px; width: 560px; height: 210px; }
  .headline-boat {
    position: absolute; left: 0; top: 0;
    font-family: "Montserrat", sans-serif; font-weight: 900; font-size: 150px; line-height: 1;
    letter-spacing: -9px;
    background: linear-gradient(90deg, var(--orange), var(--coral) 60%, var(--pink));
    -webkit-background-clip: text; background-clip: text; color: transparent;
    filter: drop-shadow(4px 4px 0 var(--white));
  }
  .headline-party {
    position: absolute; left: 70px; top: 28px;
    font-family: "Allura", cursive; font-size: 170px; line-height: 1;
    color: var(--white); transform: rotate(-3deg);
  }
  .drinks-photo {
    position: absolute; left: 531px; top: 533px; width: 224px; height: 214px;
    background: linear-gradient(135deg, #e8731f 0%, #f3a33c 40%, #b9d36a 70%, #8fb63a 100%);
    border-radius: 20px 20px 40px 40px;
  }
  .date-plank {
    position: absolute; left: 141px; top: 752px; width: 460px; height: 66px;
    background: linear-gradient(180deg, var(--plank) 0%, var(--plank-dark) 100%);
    transform: rotate(-1.5deg);
    clip-path: polygon(2% 8%, 99% 0, 100% 90%, 0 100%);
  }
  .date {
    position: absolute; left: 141px; top: 751px; width: 460px; text-align: center;
    font-family: "Montserrat", sans-serif; font-weight: 800; font-size: 68px;
    letter-spacing: 6px; color: var(--white); line-height: 68px;
  }
  .featuring {
    position: absolute; left: 0; right: 0; top: 840px; text-align: center;
    font-family: "Montserrat", sans-serif; font-weight: 800; font-size: 16px; line-height: 20px;
    letter-spacing: 4px; color: var(--white);
  }
  .lineup {
    position: absolute; left: 0; right: 0; top: 866px; text-align: center;
    font-family: "Montserrat", sans-serif; font-weight: 500; font-size: 15px;
    letter-spacing: 3.4px; line-height: 26px; color: var(--white);
  }
</style>
</head>
<body>
<div class="canvas">
  <div class="poster">
    <div class="brand"><span class="brand-dot"></span>Lantern Tide</div>
    <div class="presents">PRESENTS</div>
    <div class="boat-photo" role="img" aria-label="Party boat full of guests cruising past rocky islands on a turquoise sea"></div>
    <div class="headline">
      <div class="headline-boat">BOAT</div>
      <div class="headline-party">party</div>
    </div>
    <div class="drinks-photo" role="img" aria-label="Orange spritz and mojito cocktails with citrus halves"></div>
    <div class="date-plank"></div>
    <div class="date">18.05.22</div>
    <div class="featuring">FEATURING</div>
    <div class="lineup">
      IBIZA FAMOUS RESIDENT DJ’S<br>
      PROFESSIONAL DANCERS PERFORMING<br>
      A FIRE SHOW:LED SHOW AND ACT<br>
      AS VIP HOSTESSES FOR GUESTS.
    </div>
  </div>
</div>
</body>
</html>
```